Upmarket Dessert Lounge needs a Business Card Design

We are an upmarket dessert lounge needing a business card to match our image.

We want something that is simple yet beautiful, feminine, classy, sophisticated and elegant. We want it to stand out and don't mind if it is bold.

The design should include our logo and colours of red or maroon with gold highlights. We don't mind if black is used.

Marlow & Quince

Target Market(s)

For those who like to indulge or treat themselves and give in to their temptations on good quality desserts.

Industry/Entity Type

Business

Requirements
Must have
• Must include our logo and our name

Marlow & Quince

M & Q

```html
<!DOCTYPE html>
<html lang="en">
<head>
<meta charset="utf-8">
<title>Marlow &amp; Quince — Business Card</title>
<link rel="stylesheet" href="https://fonts.googleapis.com/css2?family=Crimson+Text:wght@400;600;700&display=swap">
<style>
  :root {
    --backdrop: #e9e4de;
    --card-black: #0b0707;
    --maroon: #7a1218;
    --maroon-deep: #3d0a0e;
    --rose-dark: #4a0b10;
    --rose-mid: #6e1219;
    --cream: #f1dfb4;
    --label-red: #9b1b22;
  }
  html, body {
    margin: 0;
    width: 1200px;
    height: 880px;
    overflow: hidden;
    background: var(--backdrop);
  }
  .canvas {
    width: 1200px;
    height: 880px;
    display: flex;
    flex-direction: column;
    align-items: center;
    justify-content: center;
    gap: 40px;
  }
  .card {
    display: block;
    width: 680px;
    height: 390px;
    box-shadow: 0 10px 24px rgba(0,0,0,0.25);
  }
  .card-base { fill: var(--card-black); }
  .frame-line { fill: none; stroke: var(--cream); stroke-width: 2; }
  .pattern-area { fill: var(--maroon-deep); }
  .brand-name {
    font-family: "Crimson Text", serif;
    font-weight: 400;
    fill: var(--cream);
    font-size: 40px;
    letter-spacing: 3px;
  }
  .monogram {
    font-family: "Crimson Text", serif;
    font-weight: 400;
    fill: var(--cream);
    font-size: 56px;
  }
  .sweep-line { fill: none; stroke: var(--cream); stroke-width: 3; }
  .sweep-band { fill: none; stroke: var(--maroon); stroke-width: 8; }
  .contact-label {
    font-family: "Crimson Text", serif;
    font-weight: 700;
    fill: var(--label-red);
    font-size: 21px;
  }
  .contact-value {
    font-family: "Crimson Text", serif;
    font-weight: 400;
    fill: var(--cream);
    font-size: 22px;
  }
</style>
</head>
<body>
<main class="canvas">

  <!-- Card back: monogram, rose field, contact details -->
  <svg class="card card-back" viewBox="0 0 680 390" xmlns="http://www.w3.org/2000/svg">
    <defs>
      <linearGradient id="rose-field-tone" x1="0" y1="0" x2="1" y2="1">
        <stop offset="0" stop-color="var(--rose-dark)"/>
        <stop offset="0.6" stop-color="var(--rose-mid)"/>
        <stop offset="1" stop-color="var(--rose-dark)"/>
      </linearGradient>
    </defs>
    <rect class="card-base" width="680" height="390"/>
    <path class="rose-field" role="img" aria-label="Dark red rose illustration"
          fill="url(#rose-field-tone)"
          d="M170,0 H680 V248 C410,214 330,118 188,96 C176,64 172,32 170,0 Z"/>
    <path class="sweep-band" d="M188,110 C330,132 410,228 680,262"/>
    <path class="sweep-line" d="M188,98 C330,120 410,216 680,250"/>
    <text class="monogram" x="92" y="118" text-anchor="middle">M&amp;Q</text>

    <g class="contact-block">
      <text class="contact-label" x="250" y="306">Phone:</text>
      <text class="contact-label" x="250" y="334">E-mail:</text>
      <text class="contact-label" x="250" y="362">Website:</text>
      <text class="contact-value" x="360" y="306">+00 123 456 789</text>
      <text class="contact-value" x="360" y="334">office@domain.com</text>
      <text class="contact-value" x="360" y="362">www.domain.com</text>
    </g>
  </svg>

  <!-- Card front: framed pattern field with brand name -->
  <svg class="card card-front" viewBox="0 0 680 390" xmlns="http://www.w3.org/2000/svg">
    <rect class="card-base" width="680" height="390"/>
    <rect class="frame-line" x="14" y="14" width="652" height="362"/>
    <rect class="frame-line" x="22" y="22" width="636" height="346"/>
    <rect class="pattern-area" role="img" aria-label="Maroon diamond damask pattern"
          x="32" y="32" width="616" height="326"/>
    <text class="brand-name" x="340" y="208" text-anchor="middle">MARLOW &amp; QUINCE</text>
  </svg>

</main>
</body>
</html>
```